Velvet Arc Car Detailing Brochure

I would like a trifold brochure designed for my car detailing business. The background has to be full black or mostly black with some designing using only colors present in our logo.

Front page must have our logo and name, list of services, a photo and mybe our phone number but no long text.

Inside I want to present each service one by one with its description and a photo representing/showing each service. (I will provide the text below). For photos, use stock photos and I will add come of mines already too.

On the back of the brochure I want to have contact & info: phone number, opening hours, address, website, Instagram.

Outside left I want the text About us and photo/design.

I want the brochure to be neat, professional, easy to read, but at the same time not too boring.

Text:
1. About us
a. the ultimate destination for car care in Geneva. We provide personalized, detail-oriented services that bring out the best in your car. With our expert techniques and dedicated approach, we ensure that your car receives the utmost care and attention. Experience a place where passion meets precision and let us create an exceptional car care experience designed just for you.
2. Services:

DETAILING & HAND WASH

• Comprehensive exterior & interior care
• Personalisation and tailored cleaning packages
• Decontamination
• Premium products
• Attention to detail for a perfect finish

POLISHING

• Eliminates scratches, holograms
• Revives and protects paint
• Ensures lasting gloss
• Enhances paint life
• Preserves car’s value and beauty

CERAMIC TREATMENT

• Durable paint protection
• Water-repellent (hydrophobic) effect
• Easier cleaning, enhanced shine
• Long-term surface safeguarding
• Shields against environmental impacts

DRY ICE WASH

• Innovative, waterless method
• Safe for all car parts
• Deep cleans, removes odors
• Allergen-free, antibacterial
• Gentle, effective
• Advanced cleaning technology

COVERING

• Personalized vehicle styling
• More than 150 colours available
• Clean cut without using a cutter
• High-quality, durable materials
• Custom designs available

PROTECTION FILM

• Invisible, durable shield
• Self-healing technology
• 10-year warranty by RQ FOLV

DETAILING BOUTIQUE

• Premium brands available
• Buy on site during your visit
• Granite Assembly, Pip Autos, DRAV Norra
• Essential for at-home car care
• Perfect for quick touch-ups
(for these three brands you can put their logos

Target Market(s)

Our target market includes car owners of all price ranges, with a special focus on those who are passionate about their vehicles. We cater to clients who value excellent service and results, and seek to maintain their cars in pristine condition.

Industry/Entity Type

Automobile / Car detailing

Colors

Designer to choose colors to be used in the design.

Requirements
Must have
• Brand Consistency: The brochure must adhere to our brand colors and style, particularly utilizing the colors present in our logo. Trifold Layout: The design must be specifically tailored for a trifold brochure format. Legibility: Text must be easy to read against the mostly black background, with appropriate font size and style. Professional Look and Feel: The overall design must convey professionalism while being engaging and not overly complex. Photo representation: each service description should have a phot presenting it.
Should not have
• Overcrowded Design: Avoid cluttering with too much text or too many images. The layout should be clean and easy to navigate. Cartoonish Fonts or Graphics: Avoid using unprofessional or casual fonts and graphics that do not align with the upscale and professional image of our business. Distracting Backgrounds: The background should complement and not overpower the content. Stick to the theme of mostly black with design elements from our logo.

```html
<!DOCTYPE html>
<html lang="fr">
<head>
<meta charset="utf-8">
<title>Velvet Arc Car Detailing – Brochure</title>
<link rel="stylesheet" href="https://fonts.googleapis.com/css2?family=Poppins:wght@400;500;600&family=Michroma&display=swap">
<style>
:root{
  --page:#b9bfcb;
  --ink:#0f0e13;
  --ink-soft:#1a1920;
  --pink:#e8158f;
  --blue:#2b8fe8;
  --violet:#7b3fd2;
  --white:#ffffff;
  --grey:#d9d9de;
}
*{margin:0;padding:0;box-sizing:border-box}
html,body{width:800px;height:1200px;overflow:hidden}
body{background:var(--page);font-family:"Poppins",sans-serif;color:var(--white);position:relative}
.sheet{position:absolute;left:93px;width:614px;height:474px;background:radial-gradient(ellipse at 50% 40%,#25232b 0%,var(--ink) 70%);overflow:hidden}
.sheet--outside{top:80px}
.sheet--inside{top:600px}
.abs{position:absolute}
.photo{position:absolute}

/* outside: about */
.about-photo{left:0;top:0;width:217px;height:240px;background:linear-gradient(135deg,#d8257f 0%,#3a4fb8 35%,#1d3a9a 60%,#0f0e13 100%)}
.about-title{left:18px;top:244px;font-family:"Michroma",sans-serif;font-size:13.5px;letter-spacing:.3px;white-space:nowrap}
.about-title em{font-style:normal;color:var(--pink)}
.about-text{left:18px;top:270px;width:180px;font-size:9.6px;line-height:11.2px;color:var(--white)}
.about-text p{margin-bottom:11px}
.about-text .accent{color:var(--blue)}

/* outside: contact */
.hours-band{left:223px;top:80px;width:179px;height:19px;background:linear-gradient(90deg,rgba(43,143,232,.2),var(--blue) 15%,var(--blue) 85%,rgba(43,143,232,.2));display:flex;align-items:center;justify-content:center;font-size:10.5px;font-weight:500;letter-spacing:.4px}
.hours-box{left:226px;top:111px;width:164px;height:32px;border:1px solid var(--pink);border-radius:4px;text-align:center;font-size:7.4px;letter-spacing:.8px;line-height:9.5px;padding-top:6px;font-weight:500}
.hours-box .day-blue{color:var(--blue)}
.hours-box .day-pink{color:var(--pink)}
.brand-ring{border-radius:50%;border:2.5px solid var(--violet)}
.brand-ring--small{left:279px;top:164px;width:54px;height:54px}
.brand-name--small{left:246px;top:222px;width:120px;text-align:center;font-size:11px;line-height:13px;letter-spacing:.3px}
.contact-title{left:226px;top:274px;width:160px;text-align:center;font-family:"Michroma",sans-serif;font-size:9.5px;letter-spacing:1px}
.contact-list{left:206px;top:288px;width:200px;text-align:center;font-size:8.6px;font-weight:500}
.contact-item{display:flex;flex-direction:column;align-items:center;margin-bottom:5px}
.contact-icon{width:12px;height:12px;border-radius:50%;background:var(--white);display:flex;align-items:center;justify-content:center;margin-bottom:2px}
.contact-item span{line-height:10px}

/* outside: cover */
.brand-ring--large{left:469px;top:27px;width:86px;height:86px;border-width:4px}
.brand-name--large{left:432px;top:118px;width:160px;text-align:center;font-size:17px;line-height:21px;letter-spacing:.5px}
.cover-photo{left:371px;top:160px;width:243px;height:220px;background:radial-gradient(ellipse at 55% 40%,#2c3a66 0%,#15182a 45%,transparent 70%),linear-gradient(160deg,transparent 30%,#2a6fd8 55%,#c0209a 75%,transparent 95%)}
.service-grid{left:420px;top:342px;width:194px}
.service-chip{position:absolute;width:60px;text-align:center;font-size:5.9px;font-weight:600;line-height:7px;letter-spacing:.2px}
.service-chip svg{display:block;margin:0 auto 3px}

/* inside */
.svc-photo{width:138px;height:56px}
.svc{position:absolute}
.svc-head{display:flex;align-items:center;gap:8px}
.svc-title{font-size:10.5px;font-weight:500;line-height:11px;letter-spacing:.2px}
.svc-list{list-style:none;margin-top:7px;margin-left:13px;font-size:7.2px;line-height:8.4px;color:var(--grey)}
.svc-list li{position:relative;padding-left:12px}
.svc-list li::before{content:"";position:absolute;left:0;top:3px;width:2.5px;height:2.5px;border:.6px solid var(--grey);border-radius:50%}
.partners{left:220px;top:108px;width:180px;height:34px}
.partner{position:absolute;font-family:"Poppins",sans-serif;white-space:nowrap;color:var(--white)}
.suv-photo{left:213px;top:160px;width:401px;height:124px;background:radial-gradient(ellipse at 65% 50%,#1e8a8c 0%,#104550 35%,transparent 65%),linear-gradient(90deg,transparent 0%,#c0209a 25%,#2b8fe8 45%,transparent 80%)}
</style>
</head>
<body>

<!-- outside spread -->
<section class="sheet sheet--outside" aria-label="Extérieur de la brochure">
  <div class="photo about-photo" role="img" aria-label="Photo d'une voiture de sport bleue dans un atelier éclairé de néons roses et bleus"></div>
  <h2 class="abs about-title">Qui Nous <em>Sommes</em></h2>
  <div class="abs about-text">
    <p>La destination ultime pour l'entretien automobile <span class="accent">à Genève.</span></p>
    <p>Nous offrons des services personnalisés et minutieux qui mettent en valeur votre voiture. Avec nos techniques expertes et notre engagement profond, nous assurons un traitement de haute qualité et un soin méticuleux à chaque véhicule.</p>
    <p>Découvrez un lieu où la passion rencontre la précision, pour une expérience de soins automobiles exceptionnelle et sur mesure.</p>
  </div>

  <div class="abs hours-band">HORAIRES D'OUVERTURE</div>
  <div class="abs hours-box">
    <div><span class="day-blue">LUNDI – VENDREDI :</span> 8:00 – 18:00</div>
    <div><span class="day-pink">SAMEDI :</span> SUR RENDEZ-VOUS</div>
  </div>
  <div class="abs brand-ring brand-ring--small"></div>
  <div class="abs brand-name--small">VELVET ARC</div>

  <h3 class="abs contact-title">CONTACTEZ-NOUS</h3>
  <div class="abs contact-list">
    <div class="contact-item">
      <div class="contact-icon"><svg width="7" height="7" viewBox="0 0 10 10"><path d="M2 1l2 2-1 1.3a6 6 0 0 0 2.7 2.7L7 6l2 2-1.3 1.3C4.5 9 1 5.5.7 2.3z" fill="var(--blue)"/></svg></div>
      <span>+41 76 418 52 30</span>
    </div>
    <div class="contact-item">
      <div class="contact-icon"><svg width="7" height="7" viewBox="0 0 10 10"><path d="M5 .5a3.3 3.3 0 0 0-3.3 3.3C1.7 6.3 5 9.5 5 9.5s3.3-3.2 3.3-5.7A3.3 3.3 0 0 0 5 .5z" fill="var(--blue)"/><circle cx="5" cy="3.8" r="1.2" fill="#fff"/></svg></div>
      <span>Chemin des Aulnes 22,<br>1228 Plan-les-Ouates</span>
    </div>
    <div class="contact-item">
      <div class="contact-icon"><svg width="7" height="7" viewBox="0 0 10 10"><rect x="1" y="2.5" width="8" height="5.5" fill="var(--blue)"/><path d="M1 2.5l4 3 4-3" stroke="#fff" stroke-width=".8" fill="none"/></svg></div>
      <span>lena@velvetarc.ch</span>
    </div>
    <div class="contact-item">
      <div class="contact-icon"><svg width="7" height="7" viewBox="0 0 10 10"><circle cx="5" cy="5" r="4" fill="none" stroke="var(--blue)" stroke-width="1"/><path d="M1 5h8M5 1c-2 2.5-2 5.5 0 8M5 1c2 2.5 2 5.5 0 8" stroke="var(--blue)" stroke-width=".8" fill="none"/></svg></div>
      <span>www.velvetarc.ch</span>
    </div>
    <div class="contact-item">
      <div class="contact-icon"><svg width="7" height="7" viewBox="0 0 10 10"><circle cx="5" cy="5" r="3.5" fill="var(--blue)"/></svg></div>
      <span>@velvetarc_gva</span>
    </div>
  </div>

  <div class="abs brand-ring brand-ring--large"></div>
  <div class="abs brand-name--large">VELVET<br>ARC</div>
  <div class="photo cover-photo" role="img" aria-label="Photo de face d'une berline noire aux phares allumés sur fond de peinture rose et bleue"></div>

  <div class="abs service-grid">
    <div class="service-chip" style="left:-10px;top:0">
      <svg width="22" height="25" viewBox="0 0 22 25"><path d="M11 1l10 5.8v11.4L11 24 1 18.2V6.8z" fill="#fff" stroke="var(--pink)" stroke-width="1.5"/><rect x="6" y="10" width="10" height="5" rx="1.5" fill="none" stroke="var(--ink)" stroke-width="1"/></svg>
      DETAILING &amp;<br>LAVAGE<br>À LA MAIN</div>
    <div class="service-chip" style="left:40px;top:0">
      <svg width="22" height="25" viewBox="0 0 22 25"><path d="M11 1l10 5.8v11.4L11 24 1 18.2V6.8z" fill="#fff" stroke="var(--pink)" stroke-width="1.5"/><rect x="6" y="10" width="10" height="5" rx="1.5" fill="none" stroke="var(--ink)" stroke-width="1"/></svg>
      POLISSAGE</div>
    <div class="service-chip" style="left:83px;top:0">
      <svg width="22" height="25" viewBox="0 0 22 25"><path d="M11 1l10 5.8v11.4L11 24 1 18.2V6.8z" fill="#fff" stroke="var(--pink)" stroke-width="1.5"/><rect x="6" y="9" width="10" height="7" fill="none" stroke="var(--ink)" stroke-width="1"/></svg>
      BOUTIQUE</div>
    <div class="service-chip" style="left:125px;top:0">
      <svg width="22" height="25" viewBox="0 0 22 25"><path d="M11 1l10 5.8v11.4L11 24 1 18.2V6.8z" fill="#fff" stroke="var(--pink)" stroke-width="1.5"/><path d="M7 15l6-6 2 2-6 6z" fill="none" stroke="var(--ink)" stroke-width="1"/></svg>
      COVERING</div>
    <div class="service-chip" style="left:5px;top:59px">
      <svg width="22" height="25" viewBox="0 0 22 25"><path d="M11 1l10 5.8v11.4L11 24 1 18.2V6.8z" fill="#fff" stroke="var(--pink)" stroke-width="1.5"/><path d="M11 8v9M7 10l8 5M15 10l-8 5" stroke="var(--ink)" stroke-width="1"/></svg>
      NETTOYAGE<br>CRYOGÉNIQUE</div>
    <div class="service-chip" style="left:60px;top:59px">
      <svg width="22" height="25" viewBox="0 0 22 25"><path d="M11 1l10 5.8v11.4L11 24 1 18.2V6.8z" fill="#fff" stroke="var(--pink)" stroke-width="1.5"/><rect x="6" y="10" width="10" height="5" rx="1.5" fill="none" stroke="var(--ink)" stroke-width="1"/></svg>
      FILM DE<br>PROTECTION</div>
    <div class="service-chip" style="left:109px;top:59px">
      <svg width="22" height="25" viewBox="0 0 22 25"><path d="M11 1l10 5.8v11.4L11 24 1 18.2V6.8z" fill="#fff" stroke="var(--pink)" stroke-width="1.5"/><rect x="6" y="10" width="10" height="5" rx="1.5" fill="none" stroke="var(--ink)" stroke-width="1"/></svg>
      TRAITEMENT<br>CÉRAMIQUE</div>
  </div>
</section>

<!-- inside spread -->
<section class="sheet sheet--inside" aria-label="Intérieur de la brochure">
  <div class="photo svc-photo" style="left:19px;top:28px;background:linear-gradient(120deg,#2a2a2e,#cfcfd4 45%,#6b6b70 75%,#1a1a1e)" role="img" aria-label="Photo d'un pinceau nettoyant une jante dans la mousse"></div>
  <div class="svc" style="left:19px;top:96px">
    <div class="svc-head">
      <svg width="26" height="24" viewBox="0 0 26 24"><rect x="3" y="8" width="18" height="8" rx="2" fill="none" stroke="var(--pink)" stroke-width="1.2"/><path d="M6 8l3-4h7l3 4" fill="none" stroke="var(--pink)" stroke-width="1.2"/><circle cx="7" cy="17" r="2" fill="none" stroke="var(--pink)"/><circle cx="17" cy="17" r="2" fill="none" stroke="var(--pink)"/></svg>
      <h3 class="svc-title">DETAILING &amp; LAVAGE<br>À LA MAIN</h3>
    </div>
    <ul class="svc-list">
      <li>Soins complets extérieur et intérieur</li>
      <li>Personnalisation et forfaits de nettoyage sur<br>mesure</li>
      <li>Décontamination</li>
      <li>Produits haut de gamme</li>
      <li>Attention aux détails pour une finition parfaite</li>
    </ul>
  </div>

  <div class="svc" style="left:19px;top:193px">
    <div class="svc-head">
      <svg width="26" height="24" viewBox="0 0 26 24"><rect x="2" y="12" width="9" height="9" fill="none" stroke="var(--pink)" stroke-width="1.2"/><rect x="13" y="12" width="9" height="9" fill="none" stroke="var(--pink)" stroke-width="1.2"/><rect x="8" y="2" width="9" height="9" fill="none" stroke="var(--pink)" stroke-width="1.2"/></svg>
      <h3 class="svc-title">NETTOYAGE<br>CRYOGÉNIQUE</h3>
    </div>
    <ul class="svc-list">
      <li>Méthode innovante sans eau</li>
      <li>Sûre pour toutes les parties de la voiture</li>
      <li>Nettoyage en profondeur, élimination des<br>odeurs</li>
      <li>Sans allergènes, antibactérien</li>
      <li>Doux, efficace</li>
    </ul>
  </div>

  <div class="photo svc-photo" style="left:24px;top:294px;width:135px;background:linear-gradient(110deg,#e58a2a,#2a2520 40%,#111 70%,#e58a2a)" role="img" aria-label="Photo d'une microfibre noire sur fond orange"></div>
  <div class="svc" style="left:19px;top:374px">
    <div class="svc-head">
      <svg width="32" height="26" viewBox="0 0 32 26"><rect x="3" y="13" width="18" height="8" rx="2" fill="none" stroke="var(--pink)" stroke-width="1.2"/><path d="M18 10l8-8M22 2l4 4" stroke="var(--pink)" stroke-width="1.2"/><circle cx="7" cy="22" r="2" fill="none" stroke="var(--pink)"/><circle cx="17" cy="22" r="2" fill="none" stroke="var(--pink)"/></svg>
      <h3 class="svc-title">TRAITEMENT<br>CÉRAMIQUE</h3>
    </div>
    <ul class="svc-list">
      <li>Protection durable de la peinture</li>
      <li>Effet hydrophobe</li>
      <li>Facilité de nettoyage, brillance améliorée</li>
      <li>Protection de surface à long terme</li>
    </ul>
  </div>

  <div class="svc" style="left:218px;top:21px">
    <div class="svc-head">
      <svg width="24" height="24" viewBox="0 0 24 24"><rect x="10" y="2" width="10" height="8" rx="1" fill="none" stroke="var(--pink)" stroke-width="1.2"/><path d="M3 12h6v10H3z" fill="none" stroke="var(--pink)" stroke-width="1.2"/><path d="M5 12V9h2v3" stroke="var(--pink)" stroke-width="1.2" fill="none"/></svg>
      <h3 class="svc-title" style="margin-left:2px">BOUTIQUE</h3>
    </div>
    <ul class="svc-list" style="margin-top:9px;margin-left:2px">
      <li>Marques premium disponibles</li>
      <li>Achetez sur place lors de votre visite</li>
      <li>Essentiel pour l'entretien de la voiture à domicile</li>
      <li>Parfait pour des retouches rapides</li>
    </ul>
  </div>

  <div class="abs partners">
    <span class="partner" style="left:0;top:0;font-size:13px;font-weight:600">DRAV Norra</span>
    <span class="partner" style="left:2px;top:19px;font-size:8px;font-weight:600">Pip Autos</span>
    <span class="partner" style="left:88px;top:2px;font-size:10px;font-weight:400;line-height:11px">Granite<br>Assembly</span>
  </div>

  <div class="photo suv-photo" role="img" aria-label="Illustration d'un SUV turquoise aux feux rouges sur fond de peinture rose et bleue"></div>

  <div class="photo svc-photo" style="left:216px;top:294px;width:140px;background:linear-gradient(120deg,#c0209a,#6a0f2a 40%,#e0e0e4 65%,#3a0a1a)" role="img" aria-label="Photo d'une pose de film coloré sur une carrosserie rouge"></div>
  <div class="svc" style="left:222px;top:369px">
    <div class="svc-head">
      <svg width="26" height="24" viewBox="0 0 26 24"><circle cx="15" cy="9" r="7" fill="none" stroke="var(--pink)" stroke-width="1.2"/><circle cx="15" cy="9" r="3" fill="none" stroke="var(--pink)"/><path d="M10 14l-7 7" stroke="var(--pink)" stroke-width="1.2"/></svg>
      <h3 class="svc-title">COVERING</h3>
    </div>
    <ul class="svc-list" style="margin-left:0">
      <li>Personnalisation du style de votre véhicule</li>
      <li>Plus de 150 couleurs disponibles</li>
      <li>Film satin, mate, texturé ou brillant</li>
      <li>Découpe nette sans utilisation du cutter</li>
    </ul>
  </div>

  <div class="photo svc-photo" style="left:422px;top:28px;background:linear-gradient(120deg,#1a1a1e,#c0209a 30%,#9aa4b8 55%,#1a1a1e)" role="img" aria-label="Photo d'une raclette posant un film de protection transparent"></div>
  <div class="svc" style="left:426px;top:92px">
    <div class="svc-head">
      <svg width="24" height="24" viewBox="0 0 24 24"><rect x="3" y="3" width="12" height="16" fill="none" stroke="var(--pink)" stroke-width="1.2"/><path d="M6 7h6M6 11h6M15 10l6 6v5H9" fill="none" stroke="var(--pink)" stroke-width="1.2"/></svg>
      <h3 class="svc-title">FILM DE PROTECTION</h3>
    </div>
    <ul class="svc-list" style="margin-left:4px">
      <li>Protection invisible sur votre carroserie</li>
      <li>Film auto-régénérant sur mesure</li>
      <li>10 ans de garantie</li>
    </ul>
  </div>

  <div class="photo svc-photo" style="left:412px;top:294px;width:133px;background:linear-gradient(110deg,#c01a2a,#555 30%,#2ab7c9 55%,#333 80%)" role="img" aria-label="Photo d'une polisseuse turquoise sur un capot"></div>
  <div class="svc" style="left:419px;top:374px">
    <div class="svc-head">
      <svg width="26" height="24" viewBox="0 0 26 24"><rect x="4" y="12" width="16" height="7" rx="2" fill="none" stroke="var(--pink)" stroke-width="1.2"/><rect x="7" y="3" width="8" height="5" fill="none" stroke="var(--pink)" stroke-width="1.2"/><path d="M11 8v4" stroke="var(--pink)" stroke-width="1.2"/></svg>
      <h3 class="svc-title">POLISSAGE</h3>
    </div>
    <ul class="svc-list" style="margin-left:0">
      <li>Élimination des rayures, hologrammes</li>
      <li>Revitalisation et protection de la peinture</li>
      <li>Amélioration de la durée de vie de la peinture</li>
      <li>Préservation de la valeur et de la beauté de la<br>voiture</li>
    </ul>
  </div>
</section>

</body>
</html>
```